PLIVET Buck Slip: Request for Donations to our Program's Development Fund

We would like to create an invitation card/double sided pamplet (about 4x9 inches) to place in orthopaedics clinics and hand/mail out to potential donors about our research program, Westmere Study Group for Joint & Muscle Health. We have attached a copy of a design we've been working with but are looking for more of a professional touch.

Target Market(s)

Patients, Donors

Industry/Entity Type

Medical And Science

Font styles to use
Other font styles liked:
• Gothan Bold, Gotham Book, Gothan, Georgia, Serif, Sans Serif

Colors
ec1f27
f78f20
ffffff
000000
333333
5c5c5c
fbed22
fbee3d
ffc214

Requirements
Must have
• Please use the visual identity standards for guidance to help with colour choice and font selection (https://www.norvalenu.example/brand/system/files/1.0-logo-visual-identity_april2017.pdf)

```html
<!DOCTYPE html>
<html lang="en">
<head>
<meta charset="utf-8">
<title>PLIVET Buck Slip</title>
<link rel="stylesheet" href="https://fonts.googleapis.com/css2?family=Merriweather:wght@700&family=Montserrat:ital,wght@0,500;0,600;0,700;0,800;1,500&display=swap">
<style>
  :root {
    --red: #ec1f27;
    --orange: #f78f20;
    --gold: #ffc214;
    --ink: #333333;
    --grey: #5c5c5c;
    --soft-grey: #7d7f7a;
    --dark-swoosh: #3a3d38;
    --stage: #2b2b2d;
    --white: #ffffff;
  }
  * { box-sizing: border-box; margin: 0; padding: 0; }
  html, body { width: 1200px; height: 1112px; overflow: hidden; }
  body {
    background: var(--stage);
    font-family: "Montserrat", Arial, sans-serif;
    position: relative;
  }
  .card {
    position: absolute;
    left: 98px;
    width: 1004px;
    height: 447px;
    overflow: hidden;
    background: linear-gradient(115deg, #e2e2e2 0%, #ffffff 35%, #f4f4f4 60%, #ffffff 75%, #dedede 100%);
  }
  .card--front { top: 99px; }
  .card--back { top: 566px; }

  .hero-photo {
    position: absolute;
    left: 0; top: 0;
    width: 620px; height: 447px;
    background:
      radial-gradient(ellipse 150px 110px at 270px 260px, #2a211c 0%, #5b3b2c 45%, rgba(160,110,90,0) 100%),
      radial-gradient(ellipse 260px 200px at 280px 290px, #c89484 0%, #a8766a 50%, rgba(150,160,180,0) 100%),
      linear-gradient(180deg, #b9bfc8 0%, #8c9aae 55%, #6b7f99 100%);
    -webkit-mask-image: linear-gradient(90deg, #000 65%, transparent 100%);
    mask-image: linear-gradient(90deg, #000 65%, transparent 100%);
  }
  .swooshes { position: absolute; left: 0; top: 0; width: 1004px; height: 447px; }

  .quote {
    position: absolute;
    right: 34px; top: 62px;
    text-align: right;
    white-space: nowrap;
    font-family: "Merriweather", Georgia, serif;
    font-weight: 700;
    font-size: 25px;
    line-height: 33.5px;
    color: var(--red);
  }
  .quote__author {
    position: absolute;
    right: 34px; top: 236px;
    font-style: italic;
    font-weight: 500;
    font-size: 22px;
    color: var(--ink);
  }

  .brand {
    position: absolute;
    left: 437px;
    display: flex;
    align-items: center;
  }
  .card--front .brand { top: 370px; }
  .card--back .brand { top: 16px; }
  .brand__name {
    width: 230px;
    font-weight: 800;
    font-size: 50px;
    letter-spacing: 1px;
    color: var(--red);
  }
  .brand__rule { width: 1px; height: 56px; background: #cfcfcf; margin: 0 14px 0 6px; }
  .brand__tagline {
    font-weight: 600;
    font-size: 17px;
    line-height: 21px;
    color: #111;
  }
  .brand__tagline span { display: block; letter-spacing: 1.6px; font-weight: 500; }

  .appeal { position: absolute; left: 47px; top: 84px; white-space: nowrap; }
  .appeal__title { font-weight: 800; font-size: 21px; line-height: 26px; color: var(--red); }
  .appeal__body { font-weight: 700; font-size: 16px; line-height: 22.5px; color: var(--soft-grey); margin-top: 1px; }
  .contact { position: absolute; left: 47px; top: 192px; color: var(--red); font-weight: 800; white-space: nowrap; }
  .contact__lead { font-size: 14.5px; }
  .contact__phone { font-size: 30px; line-height: 36px; margin-top: 2px; }
  .contact__email { font-size: 15.5px; }

  .mission { position: absolute; left: 622px; top: 144px; width: 370px; }
  .mission__lead { font-weight: 700; font-size: 17.5px; line-height: 24px; color: var(--soft-grey); }
  .mission__list { list-style: none; margin-top: 8px; }
  .mission__list li { font-weight: 800; font-size: 18.5px; line-height: 24px; color: var(--red); }
  .mission__list li::before { content: "• "; }

  .divider { position: absolute; left: 205px; top: 324px; width: 520px; height: 6px; background: #8a8d86; }
  .partner-tab {
    position: absolute; left: 713px; top: 293px;
    width: 291px; height: 38px;
    background: var(--red);
    border-radius: 22px 0 0 0;
    color: var(--white);
    font-weight: 600; font-size: 17px;
    padding: 9px 0 0 58px;
  }
  .qr-slot {
    position: absolute; left: 47px; top: 301px;
    width: 130px; height: 130px;
    border: 2px solid #8a8d86;
    background: var(--white);
    display: flex; align-items: center; justify-content: center;
    text-align: center;
    font-weight: 500; font-size: 21px; line-height: 27px; color: var(--soft-grey);
  }
  .pledge { position: absolute; left: 205px; top: 358px; font-size: 14.5px; color: var(--soft-grey); white-space: nowrap; }
  .pledge b { font-weight: 700; }
  .pledge__link { display: block; margin-top: 3px; font-weight: 700; font-size: 15px; color: var(--red); text-decoration: none; }

  .partners { position: absolute; left: 745px; top: 342px; display: flex; gap: 24px; align-items: flex-end; }
  .partner { display: flex; flex-direction: column; align-items: center; gap: 8px; font-weight: 600; font-size: 14px; line-height: 16px; text-align: center; }
  .partner__mark { width: 30px; height: 30px; }
  .partner--university { color: #111; }
  .partner--university .partner__mark { background: var(--red); }
  .partner--health { color: #1a7fc1; }
  .partner--health .partner__mark { background: #1a7fc1; }
</style>
</head>
<body>

<section class="card card--front">
  <div class="hero-photo" role="img" aria-label="Photo of cupped hands holding soil with a small green seedling"></div>
  <svg class="swooshes" viewBox="0 0 1004 447" aria-hidden="true">
    <defs>
      <linearGradient id="band-front" x1="0" x2="1" y1="0" y2="0">
        <stop offset="0" stop-color="#ec1f27"/>
        <stop offset="0.45" stop-color="#f78f20"/>
        <stop offset="1" stop-color="#ffc214"/>
      </linearGradient>
      <linearGradient id="panel-front" x1="0" x2="1" y1="0" y2="0">
        <stop offset="0" stop-color="#f2f2f2"/>
        <stop offset="0.5" stop-color="#ffffff"/>
        <stop offset="1" stop-color="#e4e4e4"/>
      </linearGradient>
    </defs>
    <path d="M220,447 C310,425 370,372 450,357 L1004,357 L1004,447 Z" fill="url(#panel-front)"/>
    <path d="M425,372 C455,338 500,318 575,318 L1004,318 L1004,357 L450,357 C440,360 432,365 425,372 Z" fill="url(#band-front)"/>
    <path d="M455,352 C370,360 320,425 250,441 L205,441 C290,425 350,350 455,342 Z" fill="#ffc214"/>
    <path d="M134,441 C200,420 260,385 318,381 C290,400 275,428 250,441 Z" fill="#3a3d38"/>
    <rect x="0" y="441" width="1004" height="6" fill="#d0d0d0"/>
  </svg>
  <blockquote class="quote">Modern medical advances have<br>helped millions of people live<br>longer, healthier lives. We owe<br>these improvements to decades of<br>investment in medical research</blockquote>
  <p class="quote__author">- Harlan Reeve</p>
  <div class="brand">
    <span class="brand__name">PLIVET</span>
    <span class="brand__rule"></span>
    <p class="brand__tagline">Westmere Study Group<span>for Joint &amp; Muscle Health</span></p>
  </div>
</section>

<section class="card card--back">
  <svg class="swooshes" viewBox="0 0 1004 447" aria-hidden="true">
    <defs>
      <linearGradient id="band-back" x1="0" x2="1" y1="0" y2="0">
        <stop offset="0" stop-color="#ec1f27"/>
        <stop offset="0.45" stop-color="#f78f20"/>
        <stop offset="1" stop-color="#ffc214"/>
      </linearGradient>
    </defs>
    <rect x="0" y="0" width="1004" height="10" fill="#d0d0d0"/>
    <path d="M250,10 L305,10 C350,45 400,88 470,92 L500,92 L500,104 L470,104 C390,100 320,50 250,10 Z" fill="#ffc214"/>
    <path d="M158,10 L250,10 C280,25 305,45 318,66 C270,45 220,20 158,10 Z" fill="#3a3d38"/>
    <path d="M445,92 C470,90 490,90 520,90 L1004,90 L1004,129 L540,129 C500,129 470,112 445,92 Z" fill="url(#band-back)"/>
  </svg>
  <div class="brand">
    <span class="brand__name">PLIVET</span>
    <span class="brand__rule"></span>
    <p class="brand__tagline">Westmere Study Group<span>for Joint &amp; Muscle Health</span></p>
  </div>

  <div class="appeal">
    <h2 class="appeal__title">We need your help!</h2>
    <p class="appeal__body">Donations help run the PLIVET<br>research program and without your support, it<br>simply wouldn’t be possible.</p>
  </div>
  <div class="contact">
    <p class="contact__lead">To learn more, talk to your surgeon or contact us:</p>
    <p class="contact__phone">Phone: 555-014-3687</p>
    <p class="contact__email">Email: westmereresearch@norvalenu.example</p>
  </div>

  <div class="mission">
    <p class="mission__lead">We are passionate Clinicians and Educators focused on</p>
    <ul class="mission__list">
      <li>EMPOWERING PATIENTS</li>
      <li>ADVANCING RESEARCH</li>
      <li>IMPROVING CLINICAL CARE</li>
    </ul>
  </div>

  <div class="divider"></div>
  <div class="partner-tab">In partnership with:</div>
  <div class="qr-slot">QR CODE<br>HERE</div>
  <p class="pledge"><b>YES, I would like to help!</b> Visit the following link:
    <a class="pledge__link" href="https://give.norvalenu.example/medicine/PLIVET">https://give.norvalenu.example/medicine/PLIVET</a>
  </p>
  <div class="partners">
    <div class="partner partner--university"><span class="partner__mark"></span>Norvale<br>University</div>
    <div class="partner partner--health"><span class="partner__mark"></span>Prairie Health<br>Services</div>
  </div>
</section>

</body>
</html>
```